Front cover for our tenth anniversary show programme

To create an eye catching tenth anniversary front cover for our programme

Moonwren presents STRIDE! 2015

date of the show Sunday 3rd May 2015

Venue The Corrimore Playhouse

please see the updated brief!

Reason: there hasn't been anything that is quite right

```html
<!DOCTYPE html>
<html lang="en">
<head>
<meta charset="utf-8">
<title>Moonwren presents STRIDE! 2015 – Programme Cover</title>
<link rel="stylesheet" href="https://fonts.googleapis.com/css2?family=Poppins:ital,wght@0,300;0,400;0,700;1,300;1,700;1,800&display=swap">
<style>
  :root {
    --night: #1a0509;
    --wine: #3c0c16;
    --ember: #8a2a3c;
    --glow: #f6c9cf;
    --pink: #e35a9c;
    --white: #ffffff;
  }
  * { margin: 0; padding: 0; box-sizing: border-box; }
  html, body { width: 849px; height: 1200px; overflow: hidden; background: var(--night); }
  .cover {
    position: relative;
    width: 849px;
    height: 1200px;
    overflow: hidden;
    font-family: "Poppins", sans-serif;
    color: var(--white);
    text-align: center;
    background:
      radial-gradient(circle at 425px 585px, rgba(255,240,242,0.9) 0, rgba(244,180,192,0.6) 90px, rgba(190,80,104,0.42) 200px, rgba(120,34,52,0.3) 340px, rgba(60,12,22,0) 560px),
      radial-gradient(ellipse 700px 900px at 425px 585px, var(--wine) 0, var(--night) 100%);
  }
  .burst {
    position: absolute;
    left: 0; top: 0;
    width: 849px; height: 1200px;
  }
  .presenter {
    position: absolute; top: 6px; left: 0; right: 0;
    font-size: 22px; font-weight: 300; font-style: italic;
  }
  .show-date {
    position: absolute; top: 58px; left: 0; right: 0;
    font-size: 32px; font-weight: 400; letter-spacing: 0.5px;
  }
  .show-title {
    position: absolute; top: 118px; left: 0; right: 0;
    font-size: 84px; font-weight: 800; font-style: italic; line-height: 1;
    letter-spacing: 1px;
  }
  .show-year {
    position: absolute; top: 198px; left: 0; right: 0;
    font-size: 84px; font-weight: 800; font-style: italic; line-height: 1;
    color: var(--pink);
  }
  .dancer {
    position: absolute;
    left: 315px; top: 360px;
    width: 220px; height: 450px;
    background: radial-gradient(closest-side, rgba(255,255,255,0.97) 0, rgba(255,250,251,0.85) 35%, rgba(255,225,232,0.4) 70%, rgba(255,220,228,0) 100%);
  }
  .brand {
    position: absolute; top: 930px; left: 0; right: 0;
    display: flex; justify-content: center; align-items: center; gap: 16px;
  }
  .brand-mark {
    width: 26px; height: 26px; border-radius: 50%;
    background: var(--pink);
  }
  .brand-name {
    font-size: 70px; font-weight: 300; line-height: 1;
    color: var(--white);
  }
  .anniversary {
    position: absolute; top: 1030px; left: 0; right: 0;
    line-height: 1;
  }
  .anniversary-lead {
    display: block; font-size: 24px; font-weight: 700;
  }
  .anniversary-years {
    display: block; margin-top: 6px;
    font-size: 46px; font-weight: 700; color: var(--pink); letter-spacing: -0.5px;
  }
  .venue {
    position: absolute; top: 1142px; left: 0; right: 0;
    font-size: 18px; font-weight: 300;
  }
</style>
</head>
<body>
  <main class="cover">
    <svg class="burst" viewBox="0 0 849 1200" aria-hidden="true">
      <defs>
        <radialGradient id="ray-fade" cx="425" cy="585" r="640" gradientUnits="userSpaceOnUse">
          <stop offset="0" stop-color="#ffeef1" stop-opacity="0.6"/>
          <stop offset="0.45" stop-color="#e08a9c" stop-opacity="0.2"/>
          <stop offset="1" stop-color="#8a2a3c" stop-opacity="0"/>
        </radialGradient>
        <filter id="ray-soften" x="-10%" y="-10%" width="120%" height="120%">
          <feGaussianBlur stdDeviation="6"/>
        </filter>
      </defs>
      <g fill="url(#ray-fade)" filter="url(#ray-soften)">
        <polygon points="425,585 405,0 435,0"/>
        <polygon points="425,585 300,0 320,0"/>
        <polygon points="425,585 530,0 552,0"/>
        <polygon points="425,585 180,0 210,0"/>
        <polygon points="425,585 640,0 672,0"/>
        <polygon points="425,585 0,60 0,100"/>
        <polygon points="425,585 849,40 849,85"/>
        <polygon points="425,585 0,270 0,300"/>
        <polygon points="425,585 849,260 849,295"/>
        <polygon points="425,585 0,440 0,480"/>
        <polygon points="425,585 849,460 849,505"/>
        <polygon points="425,585 0,600 0,630"/>
        <polygon points="425,585 849,590 849,620"/>
        <polygon points="425,585 0,770 0,810"/>
        <polygon points="425,585 849,750 849,795"/>
        <polygon points="425,585 0,1000 0,1040"/>
        <polygon points="425,585 849,980 849,1025"/>
        <polygon points="425,585 60,1200 105,1200"/>
        <polygon points="425,585 230,1200 260,1200"/>
        <polygon points="425,585 400,1200 430,1200"/>
        <polygon points="425,585 580,1200 610,1200"/>
        <polygon points="425,585 760,1200 805,1200"/>
      </g>
    </svg>

    <p class="presenter">Moonwren presents</p>
    <p class="show-date">SUNDAY 3RD MAY 2015</p>
    <h1 class="show-title">STRIDE!</h1>
    <p class="show-year">2015</p>

    <div class="dancer" role="img" aria-label="White silhouette of a ballerina in a tutu, arms raised, standing on one leg"></div>

    <div class="brand">
      <span class="brand-mark"></span>
      <span class="brand-name">Moonwren</span>
    </div>

    <p class="anniversary">
      <span class="anniversary-lead">Celebrating</span>
      <span class="anniversary-years">Ten Years</span>
    </p>

    <p class="venue">at The Corrimore Playhouse</p>
  </main>
</body>
</html>
```